Meadow Paw Web Site

We have basically a start up business that I need help with. This project is just for the web site.

Our product is a frozen raw pet food that promotes weight control, less shedding, smaller stools and an overall better health. The product is in nugget form similar to what you would see in a steak shish kabob. I only share that with you in case you want to incorporate that in the design.

We have been in business for 17 years but all of our sales have been word of mouth. We are going to be launching an infomercial this summer and I need everything stated previously to be completed before we can launch the infomercial.

We need the following (6) pages:

Home:
This is where we need to have the ability to purchase our products. Our main goal is to get the consumer to purchase our product. We have our own shopping cart so we just need to allow for the insertion of that shopping cart.

Why Raw:
This will just be a page with 4-5 paragraphs and an embedded YouTube video.

How to Use:
We will need a page with a chart (4 Columns wide with 6 rows) as well as an embedded YouTube video.

Customer Success Stories:
Allow us to add these as we move forward. I need a placeholder for an image of the customers pet and a paragraph or two explaining the situation

Where to Buy:
- Online - Find a Retailer - Find a Local Distributor - Call to Order

Contact Us:
Lantern Creek Companies, Inc.
2740 Lantern Cr
Eagan, MN 55122
(800) 555-0142

We need to provide links to our to be created... Facebook page, Twitter Account, Youtube Channel, Google circle, Blog
Updates

All, I have received many front page designs that look good.  Please notice in the brief that I need multiple pages built not just the home page.  

Thanks,

Dale

Reason: I need to see the rest of the pages. Thanks, Dale

Target Market(s)

Women between the ages of 30 & 60.

Industry/Entity Type

Shopping

```html
<!DOCTYPE html>
<html lang="en">
<head>
<meta charset="utf-8">
<title>Meadow Paw</title>
<link href="https://fonts.googleapis.com/css2?family=Open+Sans:wght@400;600;700&family=Oswald:wght@400;500&display=swap" rel="stylesheet">
<style>
:root{
  --orange:#e8731c;
  --orange-light:#f39a3c;
  --orange-dark:#c95a0e;
  --yellow:#f6c21a;
  --ink:#3a3a3a;
  --muted:#8a8a8a;
  --page:#f1f1f1;
  --panel:#ffffff;
  --line:#dcdcdc;
  --footer:#2c2c2c;
  --footer-deep:#1d1d1d;
  --footer-text:#a9a9a9;
}
*{box-sizing:border-box;margin:0;padding:0}
html,body{width:796px;height:1200px;overflow:hidden}
body{position:relative;background:var(--page);font-family:"Open Sans",sans-serif;color:var(--ink)}
.abs{position:absolute}

/* header */
.site-header{left:0;top:0;width:796px;height:112px;background:var(--panel)}
.brand{left:80px;top:22px;display:flex;align-items:center;gap:8px}
.brand-mark{width:22px;height:22px;background:var(--orange)}
.brand-name{font-weight:700;font-size:24px;color:var(--orange);letter-spacing:.2px}
.account-links{right:80px;top:10px;font-size:7.5px;color:var(--muted);letter-spacing:.3px;white-space:nowrap}
.account-links span{margin-left:6px}
.auth{right:80px;top:40px;display:flex;gap:6px}
.auth a{font-size:8px;font-weight:700;color:#fff;padding:3px 10px;border-radius:3px;text-decoration:none}
.auth .sign-in{background:var(--orange)}
.auth .register{background:var(--yellow);color:var(--ink)}
.cart{left:440px;top:75px;display:flex;align-items:center;gap:5px;font-size:7.5px;font-weight:700;color:var(--ink);white-space:nowrap}
.cart small{font-weight:400;color:var(--muted);margin-left:8px;font-size:7px}
.search{left:594px;top:70px;width:122px;height:20px;border:1px solid var(--line);border-radius:10px;background:#fafafa;font-size:7.5px;color:var(--muted);padding:4px 10px}
.search svg{position:absolute;right:7px;top:5px}

/* nav */
.main-nav{left:80px;top:114px;width:636px;height:34px;border-radius:4px;background:linear-gradient(var(--orange-light),var(--orange));display:flex;align-items:center}
.main-nav a{flex:1;text-align:center;color:#fff;font-size:11.5px;font-weight:700;text-decoration:none;border-right:1px solid rgba(255,255,255,.35);line-height:34px;white-space:nowrap}
.main-nav a:last-child{border-right:0}
.main-nav .home{flex:.8;background:var(--orange-dark);border-radius:4px 0 0 4px}

/* hero */
.hero-slide{left:80px;top:160px;width:442px;height:212px;border-radius:6px;background:linear-gradient(180deg,#8ab2c8 0%,#c7a77a 45%,#6d8d3f 100%);border:3px solid #fff;box-shadow:0 1px 4px rgba(0,0,0,.2);overflow:hidden}
.hero-caption{position:absolute;left:130px;top:114px;width:250px;color:#fff;font-family:"Oswald",sans-serif;font-size:19px;line-height:23px;text-align:center;text-shadow:0 1px 3px rgba(0,0,0,.5)}
.call-box{left:543px;top:160px;width:173px;height:212px;border-radius:6px;background:linear-gradient(180deg,#bfc8b6 0%,#8e9b70 70%);border:3px solid #fff;box-shadow:0 1px 4px rgba(0,0,0,.2);overflow:hidden}
.call-box .label{position:absolute;left:0;bottom:0;width:100%;height:42px;background:var(--orange);color:#fff;font-family:"Oswald",sans-serif;font-size:17px;line-height:42px;text-align:center}
.slider-dots{left:290px;top:384px;display:flex;gap:5px}
.slider-dots i{width:6px;height:6px;border-radius:50%;background:#c8c8c8}
.slider-dots i:first-child{background:var(--orange)}

/* content band */
.content-band{left:0;top:402px;width:796px;height:470px;background:#e7e7e7}
.side-tile{left:80px;width:172px;height:112px;background:var(--panel);border:1px solid var(--line)}
.side-tile .photo{height:72px;margin:4px;background:linear-gradient(135deg,#f4d9cf,#b88b6a)}
.side-tile p{font-size:8.5px;color:var(--orange);padding:0 6px;line-height:11px;white-space:nowrap}
.side-tile span{display:block;font-size:6.5px;color:var(--muted);padding:1px 6px;font-weight:700}

.products{left:270px;top:414px;width:446px;height:448px;background:var(--panel);border:1px solid var(--line)}
.products h2{height:24px;line-height:24px;font-size:10.5px;font-weight:700;padding-left:10px;border-bottom:2px solid var(--orange);background:#f7f7f7}
.product-grid{display:grid;grid-template-columns:repeat(4,1fr);gap:12px 12px;padding:10px}
.product .pack{height:124px;background:linear-gradient(180deg,#fafafa,#eaeaea);border:1px solid #eee;display:flex;align-items:center;justify-content:center}
.product .pack div{width:52px;height:100px;border-radius:3px}
.product .name{font-size:6.5px;color:var(--muted);margin-top:4px}
.product .row{display:flex;justify-content:space-between;align-items:center;margin-top:3px}
.product .price{font-size:10px;font-weight:700}
.product .add{font-size:6.5px;color:#fff;background:var(--orange);padding:2px 5px;border-radius:2px;font-weight:700;white-space:nowrap}

/* features */
.feature{top:882px;width:212px;height:88px;display:flex;gap:6px}
.feature .photo{width:52px;height:86px;flex:none;background:linear-gradient(160deg,#e9ddcf,#a77a55)}
.feature h3{font-family:"Oswald",sans-serif;font-weight:500;font-size:13.5px;color:var(--ink);line-height:18px;white-space:nowrap}
.feature p{font-size:7px;color:var(--muted);line-height:10px;margin-top:3px}
.feature span{display:block;font-size:6.5px;color:var(--ink);font-weight:700;margin-top:5px}

/* footer */
.site-footer{left:0;top:986px;width:796px;height:180px;background:var(--footer)}
.footer-col{top:1000px;color:var(--footer-text);font-size:7px;line-height:11px;white-space:nowrap}
.footer-col h4{color:#fff;font-size:10px;font-weight:700;margin-bottom:6px}
.footer-col .phone{display:flex;align-items:center;gap:4px;margin-top:4px}
.newsletter input{display:block;width:120px;height:16px;border:0;background:#444;margin-top:6px}
.newsletter .subscribe{display:inline-block;margin-top:5px;background:var(--orange);color:#fff;font-size:7px;font-weight:700;padding:3px 8px;border-radius:2px}
.social{display:flex;gap:4px;margin-top:6px}
.social i{width:13px;height:13px;background:#5b5b5b}
.bottom-bar{left:0;top:1166px;width:796px;height:34px;background:var(--footer-deep);color:#777;font-size:7px;line-height:34px;padding-left:80px}
</style>
</head>
<body>

<header class="abs site-header"></header>
<div class="abs brand"><span class="brand-mark"></span><span class="brand-name">Meadow Paw</span></div>
<div class="abs account-links"><span>MY ACCOUNT</span> | <span>WISH LIST</span> | <span>MY CART</span> | <span>CHECKOUT</span></div>
<div class="abs auth"><a class="sign-in" href="#">Sign in</a><a class="register" href="#">Register</a></div>
<div class="abs cart">
  <svg width="14" height="12" viewBox="0 0 14 12"><path d="M0 1h3l2 7h7l2-5H4" fill="none" stroke="#e8731c" stroke-width="1.5"/><circle cx="6" cy="10.5" r="1.2" fill="#e8731c"/><circle cx="11" cy="10.5" r="1.2" fill="#e8731c"/></svg>
  SHOPPING CART <small>(0) ITEMS</small>
</div>
<div class="abs search">Search...
  <svg width="9" height="9" viewBox="0 0 9 9"><circle cx="3.8" cy="3.8" r="2.8" fill="none" stroke="#e8731c" stroke-width="1.3"/><path d="M6 6l2.5 2.5" stroke="#e8731c" stroke-width="1.3"/></svg>
</div>

<nav class="abs main-nav">
  <a class="home" href="#">Home</a>
  <a href="#">Why Raw</a>
  <a href="#">How to Use</a>
  <a href="#">Where to Buy</a>
  <a href="#">Success Stories</a>
  <a href="#">Contact Us</a>
</nav>

<section class="abs hero-slide" role="img" aria-label="Photo of three puppies lying on a wooden table outdoors">
  <p class="hero-caption">There are many variations of passages of Lorem</p>
</section>
<aside class="abs call-box" role="img" aria-label="Photo of a small dog on grass">
  <div class="label">CALL TO ORDER</div>
</aside>
<div class="abs slider-dots"><i></i><i></i><i></i><i></i></div>

<div class="abs content-band"></div>

<article class="abs side-tile" style="top:414px">
  <div class="photo" role="img" aria-label="Photo of two spaniel dogs"></div>
  <p>Variations of passages of lorem</p><span>VIEW MORE</span>
</article>
<article class="abs side-tile" style="top:556px">
  <div class="photo" role="img" aria-label="Photo of a dog beside a food bowl"></div>
  <p>Reader will be distracted</p><span>VIEW MORE</span>
</article>
<article class="abs side-tile" style="top:698px">
  <div class="photo" role="img" aria-label="Photo of a dog eating from a bowl"></div>
  <p>Passages of Lorem Ipsum</p><span>VIEW MORE</span>
</article>

<section class="abs products">
  <h2>Hot Products</h2>
  <div class="product-grid">
    <div class="product"><div class="pack"><div role="img" aria-label="Product bag, blue and white" style="background:linear-gradient(#2d3b52,#5c6f88)"></div></div><div class="name">Literature from 45</div><div class="row"><span class="price">$ 323</span><span class="add">Add to Cart</span></div></div>
    <div class="product"><div class="pack"><div role="img" aria-label="Product bag, green and orange" style="background:linear-gradient(#4f8f3a,#d9a53a)"></div></div><div class="name">Literature from 45</div><div class="row"><span class="price">$ 323</span><span class="add">Add to Cart</span></div></div>
    <div class="product"><div class="pack"><div role="img" aria-label="Product bag, teal and white" style="background:linear-gradient(#1e6f73,#5fa6a3)"></div></div><div class="name">Literature from 45</div><div class="row"><span class="price">$ 323</span><span class="add">Add to Cart</span></div></div>
    <div class="product"><div class="pack"><div role="img" aria-label="Product bag, navy and red" style="background:linear-gradient(#1f3f86,#c0392b)"></div></div><div class="name">Literature from 45</div><div class="row"><span class="price">$ 323</span><span class="add">Add to Cart</span></div></div>
    <div class="product"><div class="pack"><div role="img" aria-label="Product bag, blue and white" style="background:linear-gradient(#2d3b52,#5c6f88)"></div></div><div class="name">Literature from 45</div><div class="row"><span class="price">$ 323</span><span class="add">Add to Cart</span></div></div>
    <div class="product"><div class="pack"><div role="img" aria-label="Product bag, green and orange" style="background:linear-gradient(#4f8f3a,#d9a53a)"></div></div><div class="name">Literature from 45</div><div class="row"><span class="price">$ 323</span><span class="add">Add to Cart</span></div></div>
    <div class="product"><div class="pack"><div role="img" aria-label="Product bag, teal and white" style="background:linear-gradient(#1e6f73,#5fa6a3)"></div></div><div class="name">Literature from 45</div><div class="row"><span class="price">$ 323</span><span class="add">Add to Cart</span></div></div>
    <div class="product"><div class="pack"><div role="img" aria-label="Product bag, navy and red" style="background:linear-gradient(#1f3f86,#c0392b)"></div></div><div class="name">Literature from 45</div><div class="row"><span class="price">$ 323</span><span class="add">Add to Cart</span></div></div>
  </div>
</section>

<div class="abs feature" style="left:80px">
  <div class="photo" role="img" aria-label="Photo of a dog sitting"></div>
  <div><h3>Find a Retailer</h3><p>It is a long established fact that a reader will be distracted by the readable content of a page.</p><span>View more</span></div>
</div>
<div class="abs feature" style="left:292px">
  <div class="photo" role="img" aria-label="Photo of a dog with a food bowl"></div>
  <div><h3>Find a Local Distributor</h3><p>It is a long established fact that a reader will be distracted by the readable content.</p><span>View more</span></div>
</div>
<div class="abs feature" style="left:504px">
  <div class="photo" role="img" aria-label="Photo of a spaniel dog"></div>
  <div><h3>Online Shop</h3><p>It is a long established fact that a reader will be distracted by the readable content of a page.</p><span>View more</span></div>
</div>

<footer class="abs site-footer"></footer>
<div class="abs footer-col" style="left:80px"><h4>Quick Links</h4>Why Raw<br>How to Use<br>Where to Buy<br>Success Stories<br>Contact Us</div>
<div class="abs footer-col" style="left:196px"><h4>Top Products</h4>Product 1<br>Product 2<br>Product 3<br>Product 4<br>Product 5<br>Product 6</div>
<div class="abs footer-col" style="left:310px"><h4>Where to Buy</h4>Online<br>Find a Retailer<br>Find a Local Distributor<br>Call to Order</div>
<div class="abs footer-col" style="left:440px"><h4>Contact Information</h4>Lantern Creek Companies, Inc.<br>2740 Lantern Cr<br>Eagan, MN 55122
  <div class="phone"><svg width="8" height="8" viewBox="0 0 8 8"><path d="M1 1l2 0 1 2-1 1a4 4 0 0 0 2 2l1-1 2 1v2C4 8 0 4 1 1z" fill="#e8731c"/></svg>(800) 555-0142</div>
</div>
<div class="abs footer-col newsletter" style="left:596px"><h4>Newsletter</h4>Get news and offers sent<br>straight to your inbox.
  <input type="text" aria-label="Email address"><span class="subscribe">Subscribe</span>
  <div class="social"><i></i><i></i><i></i><i></i><i></i></div>
</div>
<div class="abs bottom-bar">Copyright Meadow Paw © 2014. Privacy Policy</div>

</body>
</html>
```